draft # 94 and #95- Could we see the accent pink line in more of a brush stroke and could you make the logo a little bigger and the name and title smaller. Please add the website on the front of the card and add "Locally owned and operated" in the back.
draft #58
We would like to include our tag line of the front of the card "Making memories, one dip at a time!" Could we see this tagline in the same script font used in the logo. Could you also add
"Serving Millbrook & Surrounding Areas" on the back of the card, above the watermark
Mossworks-Could we see the coordinating stationery and envelopes for draft #58
Thank you all for your submissions! We are off to a good start. Please show us more options using the chocolate brown as the primary color and using pink as the accent color. Also please remember to include "Locally owned and operated." on the back of the card. (without quotation marks, of course)
We would also like to see the fountain part of the logo or the initials as a watermark on the back of the card.
We want to make sure the font on the logo is bigger than the other font size used on the rest of the card.
Draft # 54 could we see the front logo a little bigger and add Locally owned and operated on the back.
Thanks!=)

```html
<!DOCTYPE html>
<html lang="en">
<head>
<meta charset="utf-8">
<title>Rosa Fondue Stationery Set</title>
<link href="https://fonts.googleapis.com/css2?family=Lato:wght@400;700&family=Great+Vibes&display=swap" rel="stylesheet">
<style>
  :root{
    --brown:#5b1e22;
    --pink:#d62a5c;
    --paper:#ffffff;
    --ground:#eee7dc;
    --ink:#4a2a2a;
    --faint:#f3e6e8;
    --faint-dark:rgba(255,255,255,.16);
  }
  *{margin:0;padding:0;box-sizing:border-box}
  html,body{width:1200px;height:497px;overflow:hidden}
  body{background:var(--ground);font-family:"Lato",sans-serif;color:var(--ink);position:relative}
  .item{position:absolute;box-shadow:0 2px 6px rgba(60,30,20,.25);overflow:hidden}
  .card{width:192px;height:115px;border-radius:8px}
  .fill{position:absolute;inset:0;width:100%;height:100%}
  .brand{position:absolute;display:flex;align-items:center;gap:4px;font-weight:700;color:var(--brown);white-space:nowrap}
  .brand .dot{width:7px;height:7px;border-radius:50%;background:var(--pink)}
  .brand.on-dark{color:var(--paper)}
  .brand.on-dark .dot{background:var(--paper)}
  .brand.centered{left:0;right:0;justify-content:center}
  .contact{position:absolute;font-size:5px;line-height:8px;white-space:nowrap}
  .contact .name{font-size:7px;font-weight:700}
  .tagline{position:absolute;font-family:"Great Vibes",cursive;font-size:9px;line-height:10px;text-align:center;color:var(--brown)}
  .note{position:absolute;left:0;width:100%;font-size:5px;text-align:center}
  .on-dark-text{color:var(--paper)}
  .watermark{position:absolute;left:61px;top:22px;width:70px;height:70px;border-radius:50%;background:radial-gradient(circle,var(--faint-dark),rgba(255,255,255,0) 70%)}
  .watermark.light{background:radial-gradient(circle,var(--faint),rgba(243,230,232,0) 70%)}
  .letterhead{left:432px;top:29px;width:264px;height:458px;background:var(--paper)}
  .envelope{background:var(--paper)}
</style>
</head>
<body>

<!-- Business card: white front -->
<div class="item card" style="left:19px;top:48px;background:var(--paper)">
  <svg class="fill" viewBox="0 0 192 115" preserveAspectRatio="none"><path d="M112 0 C102 40 112 80 98 115 L192 115 L192 0Z" fill="var(--brown)"/><path d="M112 0 C102 40 112 80 98 115" stroke="var(--pink)" stroke-width="3" fill="none"/></svg>
  <div class="brand" style="left:8px;top:38px;font-size:12px"><span class="dot"></span>Rosa Fondue</div>
  <div class="tagline" style="left:4px;top:58px;width:92px">Making memories, one dip at a time!</div>
  <div class="contact on-dark-text" style="left:120px;top:10px"><div class="name">Jane Doe</div>Owner</div>
  <div class="contact on-dark-text" style="left:116px;top:70px">Phone: 555 0142<br>Fax: 555 0143<br>Email: hello@rosafondue.com<br>Web: www.rosafondue.com</div>
</div>

<!-- Business card: pink front -->
<div class="item card" style="left:223px;top:48px;background:var(--pink)">
  <svg class="fill" viewBox="0 0 192 115" preserveAspectRatio="none"><path d="M0 0 L96 0 C86 40 96 80 82 115 L0 115Z" fill="var(--paper)"/></svg>
  <div class="brand" style="left:6px;top:38px;font-size:12px"><span class="dot"></span>Rosa Fondue</div>
  <div class="tagline" style="left:2px;top:58px;width:84px">Making memories, one dip at a time!</div>
  <div class="contact on-dark-text" style="left:120px;top:10px"><div class="name">Jane Doe</div>Owner</div>
  <div class="contact on-dark-text" style="left:104px;top:70px">Phone: 555 0142<br>Fax: 555 0143<br>Email: hello@rosafondue.com<br>Web: www.rosafondue.com</div>
</div>

<!-- Business card backs -->
<div class="item card" style="left:19px;top:187px;background:var(--brown)">
  <div class="note on-dark-text" style="top:10px">Serving Millbrook &amp; Surrounding Areas</div>
  <div class="watermark" role="img" aria-label="Faint fountain watermark"></div>
  <div class="brand on-dark centered" style="top:48px;font-size:14px"><span class="dot"></span>Rosa Fondue</div>
  <div class="note on-dark-text" style="top:98px">Locally owned and operated</div>
</div>
<div class="item card" style="left:223px;top:187px;background:var(--pink)">
  <div class="note on-dark-text" style="top:10px">Serving Millbrook &amp; Surrounding Areas</div>
  <div class="watermark" role="img" aria-label="Faint fountain watermark"></div>
  <div class="brand on-dark centered" style="top:48px;font-size:14px"><span class="dot"></span>Rosa Fondue</div>
  <div class="note on-dark-text" style="top:98px">Locally owned and operated</div>
</div>
<div class="item card" style="left:108px;top:319px;background:var(--paper)">
  <div class="note" style="top:10px">Serving Millbrook &amp; Surrounding Areas</div>
  <div class="watermark light" role="img" aria-label="Faint fountain watermark"></div>
  <div class="brand centered" style="top:48px;font-size:14px"><span class="dot"></span>Rosa Fondue</div>
  <div class="note" style="top:98px">Locally owned and operated</div>
</div>

<!-- Letterhead -->
<div class="item letterhead">
  <svg class="fill" viewBox="0 0 264 458" preserveAspectRatio="none">
    <path d="M0 60 C18 150 2 300 14 458 L0 458Z" fill="var(--brown)"/>
    <path d="M14 60 C30 160 12 300 26 458" stroke="var(--pink)" stroke-width="3" fill="none"/>
  </svg>
  <div class="brand" style="left:26px;top:14px;font-size:14px"><span class="dot"></span>Rosa Fondue</div>
  <div class="contact" style="left:196px;top:12px">Phone: 555 0142<br>Fax: 555 0143<br>hello@rosafondue.com<br>www.rosafondue.com</div>
  <div class="watermark light" role="img" aria-label="Faint fountain watermark" style="left:62px;top:130px;width:150px;height:150px"></div>
</div>

<!-- Envelope: pink flap, back -->
<div class="item envelope" style="left:780px;top:41px;width:408px;height:134px">
  <svg class="fill" viewBox="0 0 408 134" preserveAspectRatio="none">
    <path d="M0 0 L408 0 L408 30 L204 100 L0 30Z" fill="var(--pink)"/>
  </svg>
</div>

<!-- Envelope: white, back -->
<div class="item envelope" style="left:780px;top:185px;width:408px;height:137px">
  <svg class="fill" viewBox="0 0 408 137" preserveAspectRatio="none">
    <path d="M0 0 L204 80 L408 0" stroke="#ddd" stroke-width="1" fill="none"/>
  </svg>
</div>

<!-- Envelope: brown flap, front -->
<div class="item envelope" style="left:672px;top:307px;width:300px;height:173px">
  <svg class="fill" viewBox="0 0 300 173" preserveAspectRatio="none">
    <path d="M0 0 L300 0 L300 50 C200 30 120 70 0 40Z" fill="var(--brown)"/>
    <path d="M0 44 C120 74 200 34 300 54" stroke="var(--pink)" stroke-width="3" fill="none"/>
  </svg>
  <div class="brand" style="left:12px;top:64px;font-size:11px"><span class="dot"></span>Rosa Fondue</div>
  <div class="contact" style="left:12px;top:132px">Phone: 555 0142<br>Email: hello@rosafondue.com<br>Web: www.rosafondue.com</div>
</div>

</body>
</html>
```